Brace Yourself for the 3 T's: Breakups, Romance, Molars and Toys.

I would like a book cover both front and back designed. I have included the current cover PLEASE VIEW. I have one cover in circulation with the word Dildo on it and one cover the says D... . I am opened to either- The title is Brace Yourself for the 3T's , so it is not required to have the "d's" listed.
I do not want this to look like a boring self help or I survived a divorce book. It needs to look fun.
I just returned from a book show and the feedback was mixed. Several said the front cover looked "homegrown" and "not professional" . Several thought the cover (especially the girl ) is what made them pick up the book.
I need a front cover in the middle of both. Professional yet fun and non intimidating. I want it to make a person smile or laugh when the see the book. I like the girl (art included) but she can be smaller, or redesigned if needed. I have included my photo as well. I do feel that the play on dental and dildos should be used . I am very opened to fun suggestions with these topics.

The back cover, as it is now is very wordy, I have included a shortened description,but feel free to shorten more. I also have included a few reviews, I would like at least 2 on there. The photo (included) on back needs to be way smaller, or not on the book at all.
The ISB number must be on the back (included)
I would be happy to answer any questions on this project.

Women aged 25-65

Dating

e34297
e667a6
eea4c8
f9d9e8
ffffff

• Title-Brace yourself for the 3 T's
• ( not sure if they need to be on there Divorce Dating Dentistry and Dildos)
• Name-Marla Kessington
• The color hot pink.
• A photo of me on the back (included)
• Book description (can be shortened)
• Some book reviews (included not all need to be on it)
• I am including the art work that is a characture of me - I would like her on the cover.
• A random photo of another person (headshot) on cover.

```html
<!DOCTYPE html>
<html lang="en">
<head>
<meta charset="utf-8">
<title>Brace Yourself for the 3T's — Marla Kessington</title>
<link href="https://fonts.googleapis.com/css2?family=Anton&family=Oswald:wght@500;700&display=swap" rel="stylesheet">
<style>
  :root {
    --stage: #232323;
    --cover-pink: #fba7ef;
    --band-pink: #fdb4f3;
    --title-dark: #2e2a2d;
    --title-plum: #5e0c4d;
    --author-white: #ffffff;
    --produce-green: #4f7a2c;
    --produce-deep: #2f5419;
    --figure-dark: #2a2a2a;
  }
  html, body {
    margin: 0;
    width: 1200px;
    height: 1166px;
    overflow: hidden;
    background: var(--stage);
  }
  .book-cover {
    position: absolute;
    left: 220px;
    top: 53px;
    width: 760px;
    height: 1060px;
    background: var(--cover-pink);
    overflow: hidden;
  }
  .title-art {
    position: absolute;
    inset: 0;
  }
  .title-line {
    font-family: "Anton", "Oswald", sans-serif;
  }
  .title-line--top { fill: var(--title-dark); }
  .title-line--middle { fill: var(--title-plum); }
  .subtitle {
    font-family: "Oswald", sans-serif;
    font-weight: 700;
    fill: var(--title-dark);
  }
  .author-band {
    position: absolute;
    left: 50px;
    right: 50px;
    top: 850px;
    height: 100px;
    background: var(--band-pink);
    box-shadow: 0 10px 14px -8px rgba(80, 20, 70, 0.35);
    display: flex;
    align-items: center;
    justify-content: center;
  }
  .author-name {
    margin: 0;
    font-family: "Oswald", sans-serif;
    font-weight: 700;
    font-size: 58px;
    letter-spacing: 1px;
    color: var(--author-white);
    text-transform: uppercase;
    white-space: nowrap;
  }
  .base-rule {
    position: absolute;
    left: 90px;
    right: 90px;
    top: 1008px;
    height: 3px;
    background: rgba(120, 40, 110, 0.18);
    box-shadow: 0 4px 8px rgba(120, 40, 110, 0.25);
  }
</style>
</head>
<body>
  <main class="book-cover">
    <svg class="title-art" width="760" height="1060" viewBox="0 0 760 1060" aria-labelledby="cover-title">
      <title id="cover-title">Brace Yourself for the 3T's</title>
      <text class="title-line title-line--top" x="40" y="330" font-size="330" textLength="680" lengthAdjust="spacingAndGlyphs">BRACE</text>
      <text class="title-line title-line--middle" x="40" y="600" font-size="250" textLength="680" lengthAdjust="spacingAndGlyphs">YOURSELF</text>

      <g class="silhouette" role="img" aria-label="Small dark silhouette of a woman leaning in and pushing">
        <rect x="210" y="700" width="70" height="150" rx="28" fill="var(--figure-dark)"/>
      </g>

      <g class="hero-produce" role="img" aria-label="Photo of a tall curved cucumber standing upright">
        <defs>
          <linearGradient id="produce-shade" x1="0" x2="1" y1="0" y2="0">
            <stop offset="0" stop-color="var(--produce-deep)"/>
            <stop offset="0.5" stop-color="var(--produce-green)"/>
            <stop offset="1" stop-color="var(--produce-deep)"/>
          </linearGradient>
        </defs>
        <rect x="310" y="250" width="140" height="590" rx="60" fill="url(#produce-shade)"/>
      </g>

      <text class="subtitle" x="472" y="790" font-size="46" textLength="250" lengthAdjust="spacingAndGlyphs">FOR THE 3T's</text>
    </svg>

    <div class="author-band">
      <p class="author-name">Marla Kessington</p>
    </div>
    <div class="base-rule"></div>
  </main>
</body>
</html>
```